Business Card Design for K&R Global

K&R Global designs and manufactures ball valves which are used in Oil & Gas drilling and production.

```html
<!DOCTYPE html>
<html lang="en">
<head>
<meta charset="utf-8">
<title>K&amp;R Global – Business Card</title>
<link href="https://fonts.googleapis.com/css2?family=Open+Sans:wght@400;600;700&family=Libre+Baskerville:wght@400&display=swap" rel="stylesheet">
<style>
  :root {
    --backdrop: #e4e4e4;
    --card: #ffffff;
    --ink: #1a1a1a;
    --label: #4a4a4a;
    --accent: #3f7f1f;
    --divider: #9a9a9a;
    --badge: #d9d9d9;
    --shadow: rgba(0, 0, 0, 0.22);
  }
  * { margin: 0; padding: 0; box-sizing: border-box; }
  html, body {
    width: 1200px; height: 900px; overflow: hidden;
    background: var(--backdrop);
    font-family: "Open Sans", Arial, sans-serif;
    color: var(--ink);
  }
  .canvas { position: relative; width: 1200px; height: 900px; }

  .card {
    position: absolute;
    width: 640px; height: 366px;
    background: var(--card);
    border-radius: 30px;
    box-shadow: 0 4px 14px var(--shadow);
  }
  .card--front { left: 110px; top: 60px; }
  .card--back  { left: 450px; top: 474px; }

  /* front */
  .front-brand {
    position: absolute; inset: 0;
    display: flex; align-items: center; justify-content: center; gap: 22px;
  }
  .brand-mark { width: 46px; height: 46px; background: var(--ink); flex: none; }
  .brand-name {
    font-family: "Open Sans", Arial, sans-serif;
    font-weight: 700; font-size: 56px; color: var(--ink);
    letter-spacing: 0.5px; white-space: nowrap;
  }

  /* back */
  .back-brand {
    position: absolute; left: 24px; top: 124px;
    display: flex; align-items: center; gap: 10px;
  }
  .back-brand .brand-mark { width: 22px; height: 22px; }
  .back-brand .brand-name { font-size: 25px; }

  .certification {
    position: absolute; left: 238px; top: 100px; width: 92px;
    text-align: center;
  }
  .certification__badge {
    display: block; margin: 0 auto;
    width: 64px; height: 64px; border-radius: 50%;
    background: var(--badge);
  }
  .certification__text {
    margin-top: 12px;
    font-family: "Libre Baskerville", Georgia, serif;
    font-size: 8.5px; line-height: 1.35; color: var(--ink);
    white-space: nowrap;
  }

  .divider {
    position: absolute; left: 346px; top: 40px;
    width: 1.5px; height: 290px;
    background: linear-gradient(to bottom, transparent, var(--divider) 20%, var(--divider) 80%, transparent);
  }

  .contact { position: absolute; left: 366px; top: 34px; width: 260px; }
  .contact__name { font-size: 20px; font-weight: 700; color: var(--accent); line-height: 1.1; }
  .contact__role { font-size: 16px; color: var(--ink); margin-bottom: 12px; }
  .contact__item { margin-bottom: 8px; font-size: 11.5px; line-height: 1.25; }
  .contact__label { font-weight: 700; color: var(--label); }
  .contact__value { color: var(--accent); }
</style>
</head>
<body>
<main class="canvas">

  <section class="card card--front" aria-label="Business card front">
    <div class="front-brand">
      <span class="brand-mark" aria-hidden="true"></span>
      <span class="brand-name">K&amp;R Global</span>
    </div>
  </section>

  <section class="card card--back" aria-label="Business card back">
    <div class="back-brand">
      <span class="brand-mark" aria-hidden="true"></span>
      <span class="brand-name">K&amp;R Global</span>
    </div>

    <div class="certification">
      <span class="certification__badge" role="img" aria-label="Industry certification badge"></span>
      <p class="certification__text">Specification 7-1<br>License 7-1-0487</p>
    </div>

    <div class="divider" aria-hidden="true"></div>

    <div class="contact">
      <p class="contact__name">Daniel Hargrove</p>
      <p class="contact__role">Operations Manager</p>

      <div class="contact__item">
        <p class="contact__label">Company physical address:</p>
        <p class="contact__value">2280 Cypress Bend Rd<br>Lafayette, LA 70508</p>
      </div>
      <div class="contact__item">
        <p class="contact__label">Company mailing address:</p>
        <p class="contact__value">P.O. Box 418<br>Milton, LA 70558</p>
      </div>
      <div class="contact__item">
        <p class="contact__label">Company phone No.:</p>
        <p class="contact__value">(555) 214-3370</p>
      </div>
      <div class="contact__item">
        <p class="contact__label">Company Fax No.:</p>
        <p class="contact__value">(555) 214-3371</p>
      </div>
      <div class="contact__item">
        <p class="contact__label">My email:</p>
        <p class="contact__value">daniel@krglobalvalve.com</p>
      </div>
      <div class="contact__item">
        <p class="contact__label">Company web address:</p>
        <p class="contact__value">www.krglobalvalve.com</p>
      </div>
    </div>
  </section>

</main>
</body>
</html>
```